Updating Brightkeyfolio.net site

We are looking for an experienced web designer to update our current site (brightkeyfolio.net). The Bright Key Folio (aka BKF) has more features and we would like someone to be able change the existing site to reflect those changes as well as freshen it up a bit with new images, graphics, design elements etc. We have a storyboard with all the text that I will be uploading. The format should remain the same (one page).

Target Market(s)

Title Companies

Coding

Coded - Design and coding required

Requirements
Must have
• modern design

```html
<!DOCTYPE html>
<html lang="en">
<head>
<meta charset="utf-8">
<title>Bright Key Folio</title>
<link href="https://fonts.googleapis.com/css2?family=Jost:wght@400;500;600&family=Michroma&display=swap" rel="stylesheet">
<style>
:root{
  --blue:#1a76dc;
  --blue-dark:#115bb0;
  --ink:#1f2329;
  --text:#50555c;
  --muted:#8a9099;
  --soft:#f1f3f6;
  --white:#ffffff;
}
*{box-sizing:border-box;margin:0;padding:0}
html,body{width:1200px;height:4225px;overflow:hidden}
body{position:relative;background:var(--white);font-family:'Jost',sans-serif;color:var(--text)}
.abs{position:absolute}
.heading{font-family:'Michroma',sans-serif;color:var(--ink);letter-spacing:2px;text-transform:uppercase}
.center{text-align:center;left:0;width:1200px}
.ph{position:absolute}

/* nav */
.nav{position:absolute;top:0;left:0;width:1200px;height:93px;border-bottom:1px solid #e3e6ea;background:var(--white)}
.nav a{position:absolute;top:49px;font-size:12px;font-weight:500;letter-spacing:1px;color:var(--ink);text-decoration:none;text-transform:uppercase}
.nav a.active{color:var(--blue);border-bottom:2px solid var(--blue);padding-bottom:3px}
.demo{position:absolute;top:0;left:884px;width:300px;height:34px;background:var(--blue);color:var(--white);font-size:14px;display:flex;align-items:center;justify-content:center;clip-path:polygon(6% 0,100% 0,100% 100%,0 100%)}
.brand{position:absolute;left:528px;top:0;width:144px;height:114px;background:var(--white);box-shadow:0 4px 14px rgba(0,0,0,.12);display:flex;flex-direction:column;align-items:center;justify-content:center;gap:8px;z-index:2}
.brand .mark{width:22px;height:22px;background:var(--blue)}
.brand span{font-size:14px;font-weight:600;color:var(--ink);text-align:center;line-height:1.1}

/* growth */
.growth-title{left:146px;top:716px;width:460px;font-size:16px;line-height:1.45}
.growth-sub{left:146px;top:786px;font-size:14px;color:var(--ink)}
.growth-copy{left:146px;top:822px;width:450px;font-size:13px;line-height:1.6}

/* blue bands */
.band{position:absolute;left:0;width:1200px;background:var(--blue)}
.band .heading{color:var(--white)}
.tile{position:absolute;background:linear-gradient(135deg,#8c6d55,#3e4b5c)}
.tile-label{position:absolute;bottom:12px;left:12px;color:var(--white);font-size:13px}
.what-copy{left:608px;top:1140px;width:460px;color:var(--white);font-size:13px;line-height:1.6}
.what-copy p{margin-bottom:14px}
.what-copy ul{list-style:none}
.what-copy li{position:relative;padding-left:28px;margin-bottom:12px}
.what-copy li svg{position:absolute;left:0;top:3px}

/* tabs */
.tab{position:absolute;height:32px;width:282px;background:var(--blue);color:var(--white);font-size:15px;display:flex;align-items:center;padding-left:20px;clip-path:polygon(0 0,100% 0,94% 100%,0 100%)}
.tab-line{position:absolute;height:2px;background:var(--blue)}

.sub-head{font-size:16px;font-weight:600;color:var(--ink);letter-spacing:1.5px;text-transform:uppercase}
.copy{font-size:16px;line-height:1.6;color:var(--text)}

/* phone */
.phone{position:absolute;left:746px;top:1811px;width:310px;height:358px;border:10px solid #e7e9ec;border-bottom:none;border-radius:42px 42px 0 0;background:var(--white);overflow:hidden}
.phone-bar{height:52px;border-bottom:1px solid #e1e3e6;display:flex;align-items:flex-end;justify-content:space-between;padding:0 14px 10px;font-size:13px;color:var(--blue)}
.phone-bar b{color:var(--ink);font-weight:500}
.bubble{margin:16px 0 0 14px;width:165px;background:#e9e9ee;border-radius:14px;padding:8px 10px;font-size:11px;line-height:1.35;color:var(--ink)}
.phone-input{position:absolute;bottom:0;left:0;right:0;height:36px;border-top:1px solid #e1e3e6;font-size:11px;color:var(--muted);display:flex;align-items:center;justify-content:space-between;padding:0 14px}

.step{position:absolute;top:2300px;width:330px;text-align:center;font-size:14px;line-height:1.5}
.step svg{display:block;margin:0 auto 20px}

/* portals */
.soft{position:absolute;left:0;top:2535px;width:1200px;height:972px;background:var(--soft)}
.device{position:absolute;background:#f7f8fa;border:2px solid #d9dde3;border-radius:26px;box-shadow:0 8px 24px rgba(0,0,0,.12),0 0 0 6px var(--blue) inset}
.device .screen{position:absolute;left:34px;right:34px;top:22px;bottom:22px;background:linear-gradient(135deg,#eef1f4,#d7dee6)}
.checks{position:absolute;list-style:none;font-size:13px;color:var(--text)}
.checks li{display:flex;align-items:center;gap:10px;height:37px}
.inline{position:absolute;display:flex;align-items:center;gap:10px;font-size:13px}
</style>
</head>
<body>

<svg width="0" height="0" style="position:absolute">
  <symbol id="tick" viewBox="0 0 16 16"><rect x="1" y="1" width="14" height="14" rx="2" fill="none" stroke="currentColor" stroke-width="1.6"/><path d="M4 8.5l3 3 6-7" fill="none" stroke="currentColor" stroke-width="2"/></symbol>
</svg>

<header class="nav">
  <a class="active" style="left:146px">Home</a>
  <a style="left:234px">About Us</a>
  <a style="left:352px">Increase Growth</a>
  <a style="left:704px">How It Works</a>
  <a style="left:825px">Increase Growth</a>
  <a style="left:977px">Contact Us</a>
  <div class="demo">Request A Demo</div>
  <div class="brand"><div class="mark"></div><span>Bright Key<br>Folio</span></div>
</header>

<div class="ph" role="img" aria-label="Photo of smiling homebuyers with a real estate agent outside a house" style="left:0;top:93px;width:1200px;height:527px;background:linear-gradient(90deg,#f2f2f2 0%,#c9c9c9 45%,#6f6a66 75%,#3e3b3a 100%)"></div>

<section>
  <h2 class="heading abs growth-title">Is your title company or real estate law firm committed to growth?</h2>
  <p class="abs growth-sub">Is your title company blending in instead of standing out?</p>
  <p class="abs growth-copy">The Bright Key Folio exists to enhance the closing experience for buyers, sellers, real estate agents, and lenders both pre and post-close, ultimately providing our clients a competitive advantage in the marketplace.</p>
  <div class="ph" role="img" aria-label="Businessman looking at a city skyline with rising growth arrows" style="left:610px;top:624px;width:590px;height:362px;background:linear-gradient(135deg,#c9d6e6,#4a6d95);clip-path:polygon(8% 0,100% 0,100% 100%,0 100%)"></div>
</section>

<section class="band" style="top:992px;height:608px">
  <h2 class="heading abs center" style="top:88px;font-size:20px">What is brightkeyfolio.com?</h2>
</section>
<div class="tile" role="img" aria-label="Happy buyers and sellers holding house keys" style="left:141px;top:1144px;width:208px;height:180px"><span class="tile-label">Happy Buyers and Sellers</span></div>
<div class="tile" role="img" aria-label="Happy lender relaxing at his desk" style="left:353px;top:1144px;width:210px;height:180px;background:linear-gradient(135deg,#b7c4d1,#51606f)"><span class="tile-label">Happy Lenders</span></div>
<div class="tile" role="img" aria-label="Happy real estate agents smiling in the office" style="left:141px;top:1328px;width:422px;height:176px;background:linear-gradient(135deg,#d7dde4,#5c6d80)"><span class="tile-label">Happy Real Estate Agents</span></div>
<div class="abs what-copy">
  <p>Put quite simply, the Bright Key Folio keeps all parties to a transaction happy, so they return for more repeat business and referrals.</p>
  <p>The Bright Key Folio is an innovative pre and post-close technology that is uniquely designed to accomplish three things:</p>
  <ul>
    <li><svg width="16" height="16"><use href="#tick" color="#fff"/></svg>Keep all parties to the transaction properly informed of the progress of the closing process by providing SMS texts or emails at important milestones</li>
    <li><svg width="16" height="16"><use href="#tick" color="#fff"/></svg>Keep all parties educated and informed through buyer/seller and agent/lender portals for all their transactions.</li>
    <li><svg width="16" height="16"><use href="#tick" color="#fff"/></svg>More repeat business and referrals for all parties with automated post-close marketing.</li>
  </ul>
  <p>Providing this enhanced experience will allow you to differentiate yourself from the competition and drive more business to your title company or real estate law firm.</p>
</div>

<section>
  <h2 class="heading abs center" style="top:1755px;font-size:19px">How it works</h2>
  <div class="tab-line" style="left:141px;top:1822px;width:1000px;background:#cfe0f5;height:1px"></div>
  <div class="tab" style="left:141px;top:1806px">Pre-close Technology</div>
  <div class="abs" style="left:146px;top:1892px;width:14px;height:14px;border-radius:50%;background:var(--blue)"></div>
  <h3 class="abs sub-head" style="left:176px;top:1888px">Milestone SMS Text Alerts</h3>
  <p class="abs copy" style="left:192px;top:1930px;width:500px">Did you know that the number one complaint by buyers, sellers, real estate agents and lenders is that they were not properly informed during the closing process?</p>
  <div class="abs" style="left:176px;top:2061px;width:14px;height:14px;border-radius:50%;border:2px solid var(--blue)"></div>
  <p class="abs copy" style="left:192px;top:2055px;color:var(--blue);font-weight:500">Don't they deserve better?</p>
  <p class="abs copy" style="left:192px;top:2090px;width:500px">With BKF Milestones, we solve this problem and keep all parties to a transaction informed.</p>

  <div class="phone">
    <div class="phone-bar"><span>&lsaquo; Messages</span><b>Maple Realtors</b><span>Details</span></div>
    <div class="bubble">Great news from Harbor Title. For property 1180 Meadow Lane, we have received the earnest money. The next step is to deliver title report. You will be notified when this next step has been completed. Stay tuned! Thanks Harbor Title Co.</div>
    <div class="phone-input"><span>Text Message</span><span style="color:var(--blue)">Send</span></div>
  </div>

  <h2 class="heading abs center" style="top:2222px;font-size:19px">How does it work?</h2>
  <div class="step" style="left:75px">
    <svg width="64" height="56" viewBox="0 0 64 56" fill="none" stroke="#1a76dc" stroke-width="2"><path d="M4 50h56M8 50l12-22 14 10 22-28"/><path d="M46 10h10v10"/><circle cx="34" cy="38" r="3"/></svg>
    Title company provides up to 8<br>milestones per transaction type</div>
  <div class="step" style="left:387px">
    <svg width="64" height="56" viewBox="0 0 64 56" fill="none" stroke="#1a76dc" stroke-width="2"><rect x="6" y="14" width="52" height="36" rx="3"/><path d="M6 16l26 20 26-20"/><circle cx="32" cy="12" r="8"/><path d="M29 12l2 2 4-4"/></svg>
    During the transaction, all parties to the transaction are provided milestone text messages or emails informing them of the milestone reached</div>
  <div class="step" style="left:773px">
    <svg width="64" height="56" viewBox="0 0 64 56" fill="none" stroke="#1a76dc" stroke-width="2"><rect x="16" y="4" width="32" height="44" rx="2"/><path d="M22 14h20M22 20h20M22 26h14"/><circle cx="44" cy="42" r="9"/><path d="M40 42l3 3 5-6"/></svg>
    Each text or email signify the property address, the milestone completed, and the next milestone</div>
</section>

<section>
  <div class="soft"></div>
  <div class="device" style="left:155px;top:2620px;width:394px;height:366px"><div class="screen" role="img" aria-label="Buyer portal screen with transaction information beside a property map"></div></div>
  <div class="tab-line" style="left:480px;top:2644px;width:140px;height:1px;background:#c7cdd5"></div>
  <div class="tab" style="left:614px;top:2628px">Pre-Close Portals</div>
  <p class="abs" style="left:614px;top:2700px;width:460px;font-size:14px;line-height:1.5">Pre-Close portal for all parties involved in the transaction keeping everyone informed and on the same page.</p>
  <h3 class="abs sub-head" style="left:614px;top:2768px">Buyer and Seller Portal</h3>
  <ul class="checks" style="left:620px;top:2798px">
    <li><svg width="16" height="16"><use href="#tick" color="#1a76dc"/></svg>Mapping of property</li>
    <li><svg width="16" height="16"><use href="#tick" color="#1a76dc"/></svg>Milestone Timeline</li>
    <li><svg width="16" height="16"><use href="#tick" color="#1a76dc"/></svg>Document Sharing</li>
    <li><svg width="16" height="16"><use href="#tick" color="#1a76dc"/></svg>Moving wishlist</li>
    <li><svg width="16" height="16"><use href="#tick" color="#1a76dc"/></svg>Contact information and pictures of all parties to the transaction</li>
  </ul>
  <ul class="checks" style="left:817px;top:2798px">
    <li><svg width="16" height="16"><use href="#tick" color="#1a76dc"/></svg>Transaction information</li>
    <li><svg width="16" height="16"><use href="#tick" color="#1a76dc"/></svg>Secure Wiring Instructions</li>
    <li><svg width="16" height="16"><use href="#tick" color="#1a76dc"/></svg>Moving checklist</li>
    <li><svg width="16" height="16"><use href="#tick" color="#1a76dc"/></svg>FAQ of Closing Process</li>
  </ul>

  <h3 class="abs sub-head center" style="top:3040px">Real Estate Agent / Lender Portal</h3>
  <div class="inline" style="left:146px;top:3095px"><svg width="16" height="16"><use href="#tick" color="#1a76dc"/></svg>Marketing dashboard</div>
  <div class="inline" style="left:394px;top:3095px"><svg width="16" height="16"><use href="#tick" color="#1a76dc"/></svg>Mapping of Property</div>
  <div class="inline" style="left:648px;top:3095px"><svg width="16" height="16"><use href="#tick" color="#1a76dc"/></svg>Can view all transaction</div>
  <div class="inline" style="left:958px;top:3095px"><svg width="16" height="16"><use href="#tick" color="#1a76dc"/></svg>Milestone Timeline</div>

  <div class="tab" style="left:141px;top:3182px">Post-close Technology</div>
  <h3 class="abs sub-head" style="left:146px;top:3236px">Post-Close Portals</h3>
  <ul class="checks" style="left:146px;top:3264px">
    <li style="height:34px"><svg width="16" height="16"><use href="#tick" color="#1a76dc"/></svg>Mapping</li>
    <li style="height:34px"><svg width="16" height="16"><use href="#tick" color="#1a76dc"/></svg>Customized Preferred Vendors</li>
    <li style="height:34px"><svg width="16" height="16"><use href="#tick" color="#1a76dc"/></svg>Ability to upload home related documents</li>
    <li style="height:34px"><svg width="16" height="16"><use href="#tick" color="#1a76dc"/></svg>Transaction information</li>
    <li style="height:34px"><svg width="16" height="16"><use href="#tick" color="#1a76dc"/></svg>Ability to View Closing Package</li>
    <li style="height:34px"><svg width="16" height="16"><use href="#tick" color="#1a76dc"/></svg>Contact information for all parties involved in the transaction</li>
  </ul>
  <div class="device" style="left:653px;top:3178px;width:406px;height:329px"><div class="screen" role="img" aria-label="Post-close portal screen with contact cards and documents list"></div></div>
</section>

<section>
  <h2 class="heading abs center" style="top:3650px;font-size:19px">Automated thank you emails</h2>
  <p class="abs" style="left:210px;top:3700px;width:780px;text-align:center;font-size:14px;line-height:1.6">Once a transaction is completed, the BKF system automatically sends out a thank you email to the buyer, seller, real estate agents and lenders, showing your appreciation for their business.</p>
</section>

<section class="band" style="top:3831px;height:394px">
  <h2 class="heading abs center" style="top:150px;font-size:19px">Automated satisfaction surveys and reporting</h2>
  <p class="abs" style="left:210px;top:208px;width:780px;text-align:center;font-size:14px;line-height:1.6;color:var(--white)">Celebrate your successes and address concerns via the BKF automated satisfaction surveys. After closing, the buyer, seller, real estate agents, and lenders are prompted to take a short survey about their closing experience.</p>
  <div class="inline" style="left:141px;top:275px;color:var(--white)"><svg width="16" height="16"><use href="#tick" color="#fff"/></svg>All surveys are provided to the title company via email real time.</div>
  <div class="inline" style="left:606px;top:275px;color:var(--white)"><svg width="16" height="16"><use href="#tick" color="#fff"/></svg>All scores are recorded, and title company can create satisfaction reports.</div>
</section>

</body>
</html>
```